financial company web page

We are tax and financial consulting company that needs a web site. Our logo is attached. Headquarters of our company is based in Latvia, Riga. Our actual temporary web site is www.norquill.com The main purpose of our new web site is:
* to explain the benefits of doing business through Latvian LLC companies;
* provide necessary information about taxation regime in Latvia for trading and holding companies
* propose some standard schemes of using Latvian companies for various businesses.
* offer our clients other jurisdictions companies - other European, offshore, etc.
* offer our clients ecommerce solutions
* offer our client residency in Latvia and EU
Registration of a Latvian company + accounting + legal advice will be our primary product. However, web site first page should highlight 4 other important products, such as:
1 - eCommerce (here we will explain briefly what is eCommerce, how our client can use it, what are the bonuses doing business online, explain conditions of eCommerce, etc) ;
2 - Residence Permit (here we offer EU and non-EU citizens to obtain Latvian residence permit and explain the benefits of having Latvian ID card);
3 - other Jurisdictions (here we propose list of other companies registered in the countries with favorable taxation regime, i.e. UK, Hong-Kong, Canada, Panama, BVI, UAE, etc);
4 - banking (here we explain benefits of having bank account in Latvia, explaining briefly products that bank offer, etc).
Overall Website map is the following:
1. About us
2. About Latvia
3. Contacts
4. Latvian company
5. Our services
a. еCommerce
b. Resident permit (Latvia and EU)
c. Bank accounts
d. Registration and support of other jurisdictions (European companies, Low tax companies, Offshore companies)
e. Additional services (Tax advisory, Virtual office, European licenses, Accounting services, Legal address in Riga)
6. Become Partner
7. Tembrole Travel Guide
As a start point we need only first page design. If this design suits us well we will continue to work with you on other pages. We are looking for innovative, creative and professional design in line with our corporate logo and colours. We want this design to focus more on graphic, on simplicity and usability. It should be immediately clear from the first glance what the site is about, what is our key product and how to get more information if I'm interested on something.
These are website from our sector, we want to be better:
http://www.vantel-ridge.com/
http://www.qpr-harbourline.com/
http://www.dxlventurebuilders.com/
http://www.firmstarter318.co.uk/
In case you can't find our logo, please, ask I will send it to your mail. Thanks!
Target Market(s)
European, Russian or Chinesee enterpreneurs
Industry/Entity Type
Accounting
Requirements
Must have
- Web site will be on 10 languages, so somewhere must be a button/flag to switch language.
Contact information should be on every page (phone number and add Skype buttons or similar).
Search button should be available on the first page
Button Request a Call should be on every page.
Visitors should also have a possibility to download a brochure about each product (so appropriate button should be in each section).

```html
<!DOCTYPE html>
<html lang="en">
<head>
<meta charset="utf-8">
<title>Tembrole — Tax and Financial Solutions</title>
<link href="https://fonts.googleapis.com/css2?family=Arimo:wght@400;700&display=swap" rel="stylesheet">
<style>
:root{
  --navy:#0b3a6e;
  --navy-deep:#06234a;
  --blue:#1a5aa8;
  --sky:#3f7fd0;
  --text:#333;
  --muted:#777;
  --grey-btn:#d0d2d5;
  --dark-btn:#2b2b2b;
  --footer:#f6f6f6;
  --link:#2a8fd6;
}
*{box-sizing:border-box;margin:0;padding:0}
html,body{width:1200px;height:1066px;overflow:hidden}
body{font-family:"Arimo",Arial,sans-serif;color:var(--text);background:#fff;position:relative}
.abs{position:absolute}
.topline{left:0;top:0;width:1200px;height:3px;background:var(--navy)}
.header{left:0;top:3px;width:1200px;height:125px;background:linear-gradient(#f4f4f4,#fff)}
.brand{left:91px;top:23px;display:flex;align-items:center;gap:12px}
.brand-dot{width:44px;height:44px;border-radius:50%;background:var(--navy)}
.brand-name{font-size:44px;font-weight:700;color:var(--navy);letter-spacing:-.5px}
.toplinks{left:599px;top:33px;font-size:14px;font-weight:700;color:#333}
.toplinks span{color:#aaa;margin:0 10px;font-weight:400}
.search{left:824px;top:27px;width:192px;height:30px;border:1px solid #ccc;background:#fff;font-size:12px;color:#666;padding:8px 13px}
.search svg{position:absolute;right:8px;top:6px}
.lang{left:1025px;top:27px;width:85px;height:30px;border:1px solid #ccc;background:#fff;font-size:12px;padding:7px 0 0 35px}
.lang .flag{position:absolute;left:9px;top:9px;width:17px;height:11px;background:#233f8c}
.lang .flag:before{content:"";position:absolute;left:7px;top:0;width:3px;height:11px;background:#d22}
.lang .flag:after{content:"";position:absolute;left:0;top:4px;width:17px;height:3px;background:#d22}
.lang .caret{position:absolute;right:10px;top:12px;border:5px solid transparent;border-top-color:#555}
.hero{left:0;top:128px;width:1200px;height:610px;background:linear-gradient(180deg,#1655b0 0%,#2f6fc6 45%,#5c8fd0 100%)}
.hero-photo{left:78px;top:160px;width:820px;height:575px;background:linear-gradient(160deg,rgba(220,210,200,.0) 20%,rgba(190,180,170,.55) 45%,rgba(90,80,75,.7) 100%);clip-path:polygon(50% 0,62% 0,100% 100%,0 100%,0 70%)}
.hero-base{left:0;top:730px;width:1200px;height:8px;background:var(--navy-deep)}
.nav{left:91px;top:104px;width:1019px;height:53px;display:flex;background:linear-gradient(#2a64a2,#0f3b74);border:1px solid #0a2e5c;border-radius:3px 3px 0 0}
.nav a{color:#fff;font-weight:700;font-size:15px;text-decoration:none;display:flex;align-items:center;justify-content:center;border-right:1px solid #0a2e5c}
.nav a:last-child{border-right:0}
.nav .active{background:linear-gradient(#0d3568,#082a55)}
.dropdown{left:91px;top:157px;width:259px;height:190px;background:linear-gradient(#052250,#0b3774);border:1px solid #0a2e5c;border-top:1px solid #1e4d8a;border-radius:0 0 4px 4px;padding:19px 0 0 60px;list-style:none}
.dropdown li{color:#fff;font-size:14px;font-weight:700;height:33.4px}
.dropdown li:before{content:"»";margin-right:9px}
.tagline{left:727px;top:236px;font-size:27px;font-weight:700;color:#fff}
.btn-dark{background:linear-gradient(#4a4a4a,#1f1f1f);color:#fff;font-weight:700;border:1px solid #111;border-radius:4px;display:flex;align-items:center;white-space:nowrap}
.call-hero{left:728px;top:278px;width:171px;height:36px;font-size:14.5px;padding-left:12px}
.call-hero b{font-size:20px;margin-right:9px}
.tiles{left:91px;top:424px;display:grid;grid-template-columns:repeat(3,154px);grid-template-rows:repeat(2,134px);gap:3px}
.tile{background:rgba(15,15,15,.85);border-radius:4px;color:#c8c8c8;font-size:18px;font-weight:700;text-align:center;display:flex;flex-direction:column;align-items:center;justify-content:flex-end;padding-bottom:14px;line-height:21px}
.tile svg{margin-bottom:auto;margin-top:16px}
.tile.current{background:#000;color:#fff}
.why{left:565px;top:424px;width:546px;height:270px;background:rgba(12,14,18,.9);border-radius:4px}
.why h2{position:absolute;left:15px;top:12px;font-size:18px;color:#fff}
.why-photo{position:absolute;left:16px;top:45px;width:185px;height:131px;border:2px solid #fff;border-radius:5px;background:linear-gradient(120deg,#d9c2b0,#eef3f4 60%,#c9dde0)}
.why .more{position:absolute;left:16px;top:187px;font-size:14px;font-weight:700;color:#ccc}
.why .copy{position:absolute;left:218px;top:41px;width:312px;font-size:12.6px;line-height:20.8px;color:#a9a9a9;text-align:justify}
.why .copy p{margin-bottom:7px}
.dots{left:1019px;top:707px;display:flex;gap:9px}
.dots i{width:15px;height:15px;border-radius:50%;border:2px solid #fff;background:#000}
.dots i:first-child{background:var(--navy)}
.intro{left:102px;top:755px;width:722px;font-size:14px;line-height:23px;color:#6a6a6a;text-align:justify}
.brochure{left:844px;top:762px;width:255px;height:48px;font-size:15px;padding-left:14px;gap:12px}
.divider{left:91px;top:835px;width:1020px;height:1px;background:#ddd}
.partners{left:110px;top:858px;width:990px;display:flex;justify-content:space-between;align-items:center;font-size:22px;color:#8a8a8a}
.partners span:nth-child(7){font-weight:700;color:#555}
.footer{left:0;top:916px;width:1200px;height:150px;background:var(--footer);border-top:3px solid #e8e8e8}
.btn-grey{background:linear-gradient(#e4e5e7,#c2c4c7);border:1px solid #b5b7ba;border-radius:3px;color:#444;font-weight:700;font-size:16px;display:flex;align-items:center;padding-left:14px;gap:12px;white-space:nowrap}
.partner-btn{left:92px;top:940px;width:227px;height:43px}
.call-btn{left:92px;top:1001px;width:227px;height:43px}
.vline{width:1px;height:113px;background:#d5d5d5;top:937px}
.address{left:347px;top:937px;font-size:13.5px;color:#888;line-height:20px}
.address span{display:block;padding-left:60px}
.phone{left:347px;top:992px;font-size:14.5px;font-weight:700;color:#333;display:flex;gap:10px;align-items:center}
.chat{left:347px;top:1021px;font-size:14.5px;font-weight:700;color:var(--link);display:flex;gap:10px;align-items:center}
.copyright{left:579px;top:939px;font-size:12.5px;color:#444;line-height:25px}
.sitemap{left:580px;top:1008px;width:81px;height:27px;background:linear-gradient(#e6e6e6,#c9c9c9);border:1px solid #b8b8b8;border-radius:3px;font-size:12px;font-weight:700;color:#444;text-align:center;line-height:25px}
.social{left:674px;top:1006px;display:flex;gap:16px}
.social i{width:27px;height:27px;border-radius:3px;display:block}
.quick h3{font-size:17px;font-weight:400;color:#2c5c94}
.quick{left:842px;top:937px}
.quick ul{list-style:none;display:grid;grid-template-columns:143px 130px;margin-top:12px;font-size:12.5px;color:#666;row-gap:8px}
.quick li:before{content:"•";color:#999;margin-right:6px}
</style>
</head>
<body>
<div class="abs topline"></div>
<header class="abs header">
  <div class="abs brand"><span class="brand-dot"></span><span class="brand-name">Tembrole</span></div>
  <nav class="abs toplinks">About Latvia<span>|</span>About Tembrole</nav>
  <div class="abs search">Search
    <svg width="18" height="18" viewBox="0 0 18 18"><circle cx="7" cy="7" r="5" fill="none" stroke="#222" stroke-width="2.4"/><line x1="11" y1="11" x2="16" y2="16" stroke="#222" stroke-width="3"/></svg>
  </div>
  <div class="abs lang"><span class="flag"></span>Eng<span class="caret"></span></div>
</header>

<section class="abs hero"></section>
<div class="abs hero-photo" role="img" aria-label="Photo of a curved high-rise office tower against a blue sky"></div>
<div class="abs hero-base"></div>

<nav class="abs nav">
  <a class="active" style="width:258px">Latvian Company</a>
  <a style="width:294px">European company</a>
  <a style="width:240px">eCommerce</a>
  <a style="width:227px">Virtual office</a>
</nav>
<ul class="abs dropdown">
  <li>eCommerce</li><li>Resident permit</li><li>Bank accounts</li><li>Registration</li><li>Additional services</li>
</ul>

<h1 class="abs tagline">Tax and Financial Solutions</h1>
<div class="abs btn-dark call-hero"><b>»</b>REQUEST A CALL</div>

<div class="abs tiles">
  <div class="tile current">
    <svg width="50" height="50" viewBox="0 0 50 50"><path d="M3 8h8l6 26h25l5-18H14" fill="none" stroke="#ccc" stroke-width="3"/><circle cx="20" cy="42" r="4" fill="#ccc"/><circle cx="38" cy="42" r="4" fill="#ccc"/></svg>
    eCommerce</div>
  <div class="tile">
    <svg width="56" height="50" viewBox="0 0 56 50"><rect x="10" y="10" width="36" height="28" rx="3" fill="#eadfc4"/><circle cx="30" cy="34" r="6" fill="#b22"/></svg>
    Resident<br>Permit</div>
  <div class="tile">
    <svg width="60" height="50" viewBox="0 0 60 50"><path d="M6 16 30 4l24 12z" fill="#c9ced6"/><rect x="10" y="18" width="40" height="24" fill="#c9ced6"/><rect x="16" y="21" width="5" height="18" fill="#8a93a0"/><rect x="27" y="21" width="6" height="18" fill="#d9a33a"/><rect x="39" y="21" width="5" height="18" fill="#8a93a0"/><rect x="6" y="42" width="48" height="5" fill="#aeb4bd"/></svg>
    Bank<br>Accounts</div>
  <div class="tile">
    <svg width="44" height="56" viewBox="0 0 44 56"><path d="M10 24V15a12 12 0 0 1 24 0v9" fill="none" stroke="#bbb" stroke-width="5"/><rect x="5" y="24" width="34" height="28" rx="3" fill="#aaa"/></svg>
    Registration</div>
  <div class="tile">
    <svg width="64" height="56" viewBox="0 0 64 56"><line x1="10" y1="48" x2="44" y2="16" stroke="#bbb" stroke-width="7" stroke-linecap="round"/><path d="M42 6a11 11 0 1 0 14 14l-7-2-3-6z" fill="#bbb"/></svg>
    Additional<br>Services</div>
  <div class="tile">
    <svg width="50" height="46" viewBox="0 0 50 46"><ellipse cx="20" cy="16" rx="17" ry="12" fill="#8bd14a"/><ellipse cx="32" cy="26" rx="14" ry="10" fill="#e58fb6"/></svg>
    Testimonials</div>
</div>

<section class="abs why">
  <h2>Why Tembrole</h2>
  <div class="why-photo" role="img" aria-label="Photo of a consultant drawing a growth chart"></div>
  <span class="more">VIEW MORE »</span>
  <div class="copy">
    <p>Phasellus sed justo ut neque ornare venenatis lacus ut blandit. Nulla facilisis adipiscing ipsum sed bibendum. aliquam nec lobortis eget</p>
    <p>Faucibus eu tempor quis tincidunt lectus porttitor. Aliquam interdum vulputate lacus, ac facilisis leo convallis enim erat, rutrum et venenatis vel, condimentum quis sem ante ipsum primis in faucibus orci luctus et ultrices posuere cubilia Praesent gravida, elit in consequat gravida, sapien arcu facilisis leo nec commodo magna diam</p>
  </div>
</section>
<div class="abs dots"><i></i><i></i><i></i><i></i></div>

<p class="abs intro">Mauris non lacus turpis, sed tempus mauris. Mauris vehicula, odio eget faucibus facilisis, massa arcu fermentum urna, non sollicitudin magna libero at ligula. Nulla vulputate, sapien quis accumsan volutpat, nulla orci fringilla nunc, venenatis imperdiet purus diam non nibh.</p>
<div class="abs btn-dark brochure">
  <svg width="24" height="26" viewBox="0 0 24 26"><rect x="2" y="1" width="20" height="24" rx="2" fill="#fff"/><path d="M7 18l5-10 5 10" fill="none" stroke="#c22" stroke-width="2"/></svg>
  BROCHURE DOWNLOAD</div>
<div class="abs divider"></div>
<div class="abs partners"><span>Harlowe</span><span>Quintara</span><span>Brevik</span><span>Ostrel</span><span>Delvane</span><span>Marrow</span><span>Pellucid</span><span style="font-size:13px">Norvik</span><span style="font-size:16px">Talvo</span></div>

<footer class="abs footer"></footer>
<div class="abs btn-grey partner-btn">
  <svg width="30" height="20" viewBox="0 0 30 20"><circle cx="10" cy="6" r="5" fill="#333"/><circle cx="21" cy="6" r="5" fill="#555"/><path d="M1 19a9 7 0 0 1 18 0zM13 19a9 7 0 0 1 17 0z" fill="#333"/></svg>
  BECOME PARTNER</div>
<div class="abs btn-grey call-btn">
  <svg width="28" height="26" viewBox="0 0 28 26"><rect x="2" y="5" width="19" height="19" fill="none" stroke="#333" stroke-width="2"/><path d="M11 16l2-5 12-10 3 3-12 10z" fill="#333"/></svg>
  REQUEST A CALL</div>
<div class="abs vline" style="left:331px"></div>
<div class="abs address">Address : Nulla vulpate, sapien<span>quis accumsan volutpat</span></div>
<div class="abs phone">
  <svg width="20" height="18" viewBox="0 0 20 18"><path d="M3 3c2-2 4-2 5 0l1 3-2 2c1 2 3 4 5 5l2-2 3 1c2 1 2 3 0 5-6 1-15-8-14-14z" fill="#888"/></svg>
  +371 20461958</div>
<div class="abs chat">
  <svg width="21" height="21" viewBox="0 0 21 21"><rect width="21" height="21" rx="4" fill="#2a9fe0"/><path d="M5 6h11v7H9l-3 3v-3H5z" fill="#fff"/></svg>
  chat@tembrole.com</div>
<div class="abs vline" style="left:560px"></div>
<div class="abs copyright">Copyright © 2013 &nbsp; www.norquill.com<br>All rights reserved.</div>
<div class="abs sitemap">SITE MAP</div>
<div class="abs social"><i style="background:#3b5998"></i><i style="background:#3fb2e6"></i><i style="background:#1aa0dc"></i><i style="background:#c0c0c0"></i></div>
<div class="abs vline" style="left:826px"></div>
<div class="abs quick">
  <h3>Quick Links</h3>
  <ul><li>Integer lobortis</li><li>Integer lobortis</li><li>Curabitur ac</li><li>Curabitur ac</li><li>Phasellus tellus nisl</li><li>Phasellus tellus nisl</li></ul>
</div>
</body>
</html>
```